Bref créative
Business Card for A GYM
TEMPLE OF MOTION
Simple
Temple of Motion
2875 Marwick Ave Suite B
Harlow Springs, XY 00412
at Brindle Commons
contact@templeofmotionxy.com
www.templeofmotionxy.coom
Personal Training -
Group Strength & Conditioning -
Indoor Cycling
1 month Personal Training Grand Opening Special $89

```html
<!DOCTYPE html>
<html lang="en">
<head>
<meta charset="utf-8">
<title>Temple of Motion – Business Card</title>
<link href="https://fonts.googleapis.com/css2?family=Open+Sans:wght@400;600;700&display=swap" rel="stylesheet">
<style>
  :root {
    --bg: #e4e5e6;
    --slate: #4f5a5e;
    --slate-dark: #3f484b;
    --card-light: #f7f7f7;
    --card-shade: #e2e3e3;
    --gold: #e3b425;
    --ink: #3c4346;
    --white: #ffffff;
  }
  * { margin: 0; padding: 0; box-sizing: border-box; }
  html, body { width: 1200px; height: 901px; overflow: hidden; }
  body {
    background: var(--bg);
    font-family: "Open Sans", Arial, sans-serif;
    position: relative;
  }
  .card {
    position: absolute;
    width: 560px;
    height: 320px;
    border-radius: 22px;
    overflow: hidden;
    box-shadow: 0 14px 30px rgba(0,0,0,0.18);
  }
  /* back of card */
  .card-back {
    left: 80px;
    top: 90px;
    background: linear-gradient(160deg, var(--slate) 0%, var(--slate-dark) 100%);
    color: var(--white);
    text-align: center;
  }
  .back-brand {
    margin-top: 70px;
    display: flex;
    align-items: center;
    justify-content: center;
    gap: 12px;
  }
  .brand-square {
    width: 26px;
    height: 26px;
    background: var(--gold);
    flex: none;
  }
  .back-brand .brand-name {
    font-size: 20px;
    font-weight: 700;
    letter-spacing: 3px;
    color: var(--white);
  }
  .services {
    margin-top: 34px;
    list-style: none;
    font-size: 14px;
    line-height: 1.5;
  }
  .offer {
    margin-top: 22px;
    font-size: 13px;
    letter-spacing: 0.3px;
  }
  /* front of card */
  .card-front {
    left: 560px;
    top: 480px;
    background: linear-gradient(135deg, var(--card-light) 0%, var(--card-shade) 100%);
  }
  .front-wave {
    position: absolute;
    left: 0;
    bottom: 0;
    width: 560px;
    height: 140px;
  }
  .front-brand {
    position: absolute;
    left: 32px;
    top: 68px;
    display: flex;
    align-items: center;
    gap: 14px;
  }
  .front-brand .brand-square {
    width: 30px;
    height: 30px;
  }
  .front-brand .brand-name {
    font-size: 21px;
    font-weight: 700;
    letter-spacing: 2px;
    line-height: 1.15;
    color: var(--ink);
  }
  .contact {
    position: absolute;
    left: 300px;
    top: 66px;
    font-size: 13px;
    line-height: 1.35;
    color: var(--ink);
  }
  .contact address { font-style: normal; }
  .email {
    margin-top: 12px;
    display: flex;
    align-items: center;
    gap: 7px;
  }
  .website {
    position: absolute;
    right: 30px;
    bottom: 16px;
    font-size: 13px;
    letter-spacing: 2px;
    color: var(--white);
  }
</style>
</head>
<body>

  <section class="card card-back">
    <div class="back-brand">
      <span class="brand-square"></span>
      <span class="brand-name">TEMPLE OF MOTION</span>
    </div>
    <ul class="services">
      <li>Personal Training</li>
      <li>Group Strength &amp; Conditioning</li>
      <li>Indoor Cycling</li>
    </ul>
    <p class="offer">1 month Personal Training Grand Opening Special $89</p>
  </section>

  <section class="card card-front">
    <svg class="front-wave" viewBox="0 0 560 140" preserveAspectRatio="none" aria-hidden="true">
      <path d="M0 30 C 140 20, 260 90, 400 95 C 470 98, 520 92, 560 86 L560 140 L0 140 Z" fill="var(--slate)"/>
      <path d="M0 24 C 140 10, 260 78, 400 84 C 470 87, 520 82, 560 76 L560 86 C 520 94, 470 100, 400 97 C 260 92, 140 28, 0 32 Z" fill="var(--gold)"/>
    </svg>

    <div class="front-brand">
      <span class="brand-square"></span>
      <span class="brand-name">TEMPLE OF<br>MOTION</span>
    </div>

    <div class="contact">
      <address>
        2875 Marwick Ave Suite B<br>
        Harlow Springs, XY 00412<br>
        at Brindle Commons
      </address>
      <p class="email">
        <svg width="14" height="10" viewBox="0 0 14 10" aria-hidden="true">
          <rect x="0.5" y="0.5" width="13" height="9" fill="none" stroke="var(--ink)"/>
          <path d="M0.5 0.5 L7 5.5 L13.5 0.5" fill="none" stroke="var(--ink)"/>
        </svg>
        contact@templeofmotionxy.com
      </p>
    </div>

    <p class="website">www.templeofmotionxy.coom</p>
  </section>

</body>
</html>
```